Kolibri-Stube
Ich bin sehr zufrieden mit dem Flyer, Plakat und Logo, welches ich für einen zahlbaren Preis bekommen habe. quorvix hat die Korrekturvorschläge sehr gut und immer zügig umgesetzt und ein wirklich gelungenes Resultat produzier.
Zielgruppe
Logo/Sloagan: Kolibri-Stube
Branchen: Kunst/Kultur und Bildung
Ich biete eine Kolibri-Stube an, in der bis 12 Personen quartalsweise über ein Jahr hinweg an einer Erzählung ode einem Roman arbeiten. Das Genre kann frei gewählt werden. Ob Kriminal-, Fantasy oder Liebesroman, Autobiografie oder Dokufiktion, die Grundlagen eines spannenden Textes sind die selben.
Zielgruppe sind Jugendliche bis Senioren, die gerne eine lägere Erzählung oder einen Roman schreiben möchten.
Aufgabenstellung
Siehe Design-Briefing (PDF) mit Inhalt für Flyertext
Wichtig ist mir der Flyer A4 gefaltet (zu A5 oder 2x gefaltet) oder A5, alle beidseits bedruckt und je nachdem, wie sie den Inhalt verteilen möchten.
Ich bin offen für Design- und Formatvorschläge.
- Ein Plakat A4/A3, welches mit der Vorderseite des Flyers grösstenteils übereinstimmt. Wenn ich ein InDesign oder Photoshop mit Layern kriege, kann ich den Text des Plakats selber ergänzen/bearbeiten.
Ich habe neben dem Briefing und einem Foto von mir noch ein paar Bilder hochgeladen, deren Stil mir gefällt. Habe aber NICHT deren Rechte. Bilder müssten also durch Sie gefunden werden, ich kann diese aber extra bezahlen, bitte Preis dafür deklarieren.
Logo brauche ich noch keines.
Besten Dank für Ihre Bemühungen

```html
<!DOCTYPE html>
<html lang="de">
<head>
<meta charset="utf-8">
<title>Kolibri-Stube – Flyer</title>
<link rel="stylesheet" href="https://fonts.googleapis.com/css2?family=Yanone+Kaffeesatz:wght@300;400;700&display=swap">
<style>
  :root {
    --wine-deep: #420000;
    --wine: #7b0000;
    --wine-light: #8b1414;
    --rose-box: #e0bfbf;
    --ink: #111111;
    --paper: #ffffff;
    --gold: #e8b400;
    --fold-line: #c98a8a;
  }
  * { margin: 0; padding: 0; box-sizing: border-box; }
  html, body { width: 1200px; height: 848px; overflow: hidden; background: var(--wine-deep); }
  .flyer {
    position: relative; width: 1200px; height: 848px; overflow: hidden;
    font-family: "Yanone Kaffeesatz", sans-serif; font-weight: 300;
  }
  .backdrop { position: absolute; inset: 0; width: 1200px; height: 848px; }

  /* left panel: title card */
  .title-card {
    position: absolute; left: 24px; top: 414px; width: 267px; height: 410px;
    background: var(--paper); border: 3px solid var(--ink);
  }
  .title-card__name {
    position: absolute; left: 24px; top: 40px; width: 230px;
    font-weight: 400; font-size: 62px; line-height: 74px; color: var(--ink);
    letter-spacing: 4px;
  }
  .quill {
    position: absolute; left: 232px; top: 562px; width: 150px; height: 232px;
    background: #f4e3a6;
    border-radius: 70% 80% 10% 90% / 60% 70% 10% 80%;
    transform: rotate(28deg); transform-origin: center;
  }
  .ornament {
    position: absolute; width: 52px; height: 50px;
    background: rgba(232, 180, 0, 0.35); border-radius: 6px;
  }
  .ornament--card { left: 20px; top: 408px; width: 60px; height: 56px; }
  .ornament--panel-top { left: 828px; top: 64px; }
  .ornament--panel-bottom { left: 1126px; top: 776px; }
  .ornament--web-left { left: 412px; top: 766px; }
  .ornament--web-right { left: 724px; top: 776px; }

  /* middle panel: info boxes */
  .info-box {
    position: absolute; left: 424px; width: 364px;
    background: var(--rose-box); color: var(--ink);
    padding: 5px 7px; font-size: 14.5px; line-height: 17.1px;
  }
  .info-box--topics { top: 65px; height: 281px; }
  .info-box--exchange { top: 363px; height: 76px; text-align: justify; }
  .info-box--laptop { top: 456px; height: 42px; text-align: justify; }
  .topic-list { list-style: none; margin-top: 17px; }
  .topic-list li { position: relative; padding-left: 12px; }
  .topic-list li::before { content: "·"; position: absolute; left: 0; }

  .website {
    position: absolute; left: 438px; top: 780px;
    font-weight: 300; font-size: 36px; line-height: 40px; color: var(--paper);
  }

  /* right panel: slogan */
  .slogan {
    position: absolute; left: 808px; top: 86px; width: 392px;
    text-align: center; color: var(--wine);
    font-size: 82px; line-height: 102.5px;
  }
  .slogan span { display: block; }
  .slogan .light { font-weight: 300; }
  .slogan .bold { font-weight: 700; }
</style>
</head>
<body>
<main class="flyer">
  <svg class="backdrop" viewBox="0 0 1754 1240" preserveAspectRatio="none" aria-hidden="true">
    <rect width="1754" height="1240" fill="var(--wine-deep)"/>
    <polygon points="0,0 1150,0 1150,650 560,665 0,100" fill="var(--wine)"/>
    <polygon points="530,0 1050,0 1150,95 1150,530 1010,510" fill="var(--wine-light)"/>
    <polygon points="420,615 560,665 1060,1240 420,1240" fill="var(--wine-light)"/>
    <polygon points="0,1150 80,1240 0,1240" fill="var(--wine)"/>
    <line x1="590.5" y1="0" x2="590.5" y2="1240" stroke="var(--fold-line)" stroke-width="1.2"/>
    <line x1="1181.5" y1="0" x2="1181.5" y2="1240" stroke="var(--fold-line)" stroke-width="1.2"/>
  </svg>

  <section class="panel panel--cover">
    <div class="title-card">
      <p class="title-card__name">Kolibri-<br>Stube</p>
    </div>
    <div class="ornament ornament--card" role="img" aria-label="Goldenes Eckornament"></div>
    <div class="quill" role="img" aria-label="Goldene Schreibfeder als Zeichnung"></div>
  </section>

  <section class="panel panel--info">
    <div class="info-box info-box--topics">
      <p>Die Themen eines ganzen Jahres sind</p>
      <ul class="topic-list">
        <li>Kreative Übungen für den Start des Schreibprozesses</li>
        <li>Schreibspiele, um Blockaden zu lösen</li>
        <li>Bestimmung des Genres und des Stils</li>
        <li>Entwicklung der Handlung und Spannung</li>
        <li>Wahl einer Erzählperspektive und der passenden Sprache</li>
        <li>Lebendige Protagonisten, Antagonisten und Nebenfiguren</li>
        <li>Dramatische Szenen durch Emotionen</li>
        <li>Gliederung des Stoffes zu einem roten Faden</li>
        <li>Lineare und nonlineare Erzählformen</li>
        <li>Eine Dreiaktstruktur mit interessanten Spannungsbögen</li>
        <li>Korrekturen des Stils und der Grammatik</li>
        <li>Stilistische, rhetorische und literarische Mittel</li>
        <li>Autobiografische Verfremdung und Wahrhaftigkeit</li>
        <li>Die Schnittmenge zwischen Leben und Fiktion</li>
      </ul>
    </div>
    <p class="info-box info-box--exchange">Ein regelmässiger Austausch in Kleingruppen und im Plenum helfen Ihnen, Ihre Arbeit gegenseitig zu überdenken, zu korrigieren und zu erweitern. Verschiedene Textformen und exemplarische Beispiele aus der Literatur und dem Film bieten Impulse für den eigenen Text.</p>
    <p class="info-box info-box--laptop">Ein eigener Laptop mit WLAN ist von Vorteil, da wir uns damit online leicht austauschen können.</p>
    <div class="ornament ornament--web-left" role="img" aria-label="Goldenes Eckornament"></div>
    <p class="website">www.kolibri-stube.ch</p>
    <div class="ornament ornament--web-right" role="img" aria-label="Goldenes Eckornament"></div>
  </section>

  <section class="panel panel--slogan">
    <div class="ornament ornament--panel-top" role="img" aria-label="Goldenes Eckornament"></div>
    <h1 class="slogan">
      <span class="light">Sie können</span>
      <span class="light">einen</span>
      <span class="bold">geistigen</span>
      <span class="bold">Schatz in</span>
      <span class="bold">Form eines</span>
      <span class="bold">Buches</span>
      <span class="light">schenken</span>
    </h1>
    <div class="ornament ornament--panel-bottom" role="img" aria-label="Goldenes Eckornament"></div>
  </section>
</main>
</body>
</html>
```